High End Personalized Functional Medicine in Women's Health

We are adding new and exciting personalized medicine services to our Women's Health Care practice focusing on health optimization and anti-aging as well as hormone replacement therapy and need a high end brochure to educate patients about these services. We would like to see a zen-like design that has feminine appeal. Our office colors are vibrant but soothing. We have utilized the concepts of feng shui to optimize our positive energy. The exterior of the building is peach and cream and these colors would blend with that energy The final design should communicate a sense that you can take control of your health and aging.

Target Market(s)

Females age 35-65 with annual income >$75000/year

Industry/Entity Type

Health And Wellness

Logo Text

Bright Path is the company name. Our sister company is Corva Ridge Ob/Gyn

Font styles to use
Serif

Colors

Designer to choose colors to be used in the design.

Requirements
Must have
• My project must have clean lines. I like a strong feminine appearance, not a fluffy curvy feminine look. Professional appearance, Brochure would be on thicker card stock. A strong front page that makes you want to open the brochure
Nice to have
• Eye catching photos that complement our message . I am not tied to the peach and cream color recommendation, but find those colors feminine but not so cliche as pinks and purples.
Should not have
• frilly design

```html
<!DOCTYPE html>
<html lang="en">
<head>
<meta charset="utf-8">
<title>Bright Path Functional Medicine Brochure</title>
<link href="https://fonts.googleapis.com/css2?family=Oswald:wght@300;400;500&family=Montserrat:ital,wght@0,300;0,400;0,600;1,300&display=swap" rel="stylesheet">
<style>
:root{
  --peach:#ef8a6c;
  --peach-light:#f6ab90;
  --peach-deep:#de6a50;
  --cream:#fdf0ea;
  --ink:#4e4e4e;
  --white:#ffffff;
  --stage:#3a3a3a;
  --fold:#f6f6f6;
}
*{margin:0;padding:0;box-sizing:border-box}
html,body{width:1200px;height:1200px;overflow:hidden;background:var(--stage)}
.spread{position:absolute;width:660px;height:510px;background:var(--white);overflow:hidden;font-family:"Montserrat",sans-serif;color:var(--ink)}
.spread--front{left:66px;top:70px}
.spread--back{left:447px;top:628px}
.spread svg.art{position:absolute;left:0;top:0}
.block{position:absolute}
.heading{font-family:"Oswald",sans-serif;font-weight:400;text-transform:uppercase;color:var(--peach);font-size:11.5px;line-height:13px;letter-spacing:.2px}
.body-copy{font-size:5.8px;line-height:10.4px;text-align:justify;font-weight:300;overflow-wrap:break-word;hyphens:auto}
.body-copy strong{font-weight:600}
.quote-list{margin-top:5px}
.quote{margin-bottom:10px;line-height:10.6px}
.cover-question{color:var(--white);font-size:15px;line-height:20px;text-align:center;width:220px;left:0;top:22px}
.cover-title{left:461px;top:318px;font-family:"Oswald",sans-serif;text-transform:uppercase;line-height:1}
.cover-title .line-light{font-weight:300;color:var(--peach-light);font-size:28px;display:block}
.cover-title .line-bold{font-weight:500;color:var(--peach);font-size:25px;display:block;margin-top:2px}
.cover-title .line-boxed{font-weight:500;color:var(--white);background:var(--peach);font-size:25px;display:inline-block;padding:1px 3px;margin-top:4px}
.tagline{left:461px;top:412px;width:170px;font-style:italic;font-size:8.4px;line-height:11.4px;font-weight:300}
.logo-name{left:576px;top:286px;width:66px;text-align:center;font-family:"Montserrat",sans-serif;font-size:7.5px;font-weight:600;color:var(--peach)}
.symptoms-title{left:242px;top:16px;color:#7a3d2d;font-size:12px}
.symptom{position:absolute;left:242px;width:180px}
.symptom .heading{color:var(--white);font-size:12px;position:absolute;left:30px;top:5px;white-space:nowrap}
.symptom .body-copy{color:var(--white);position:absolute;left:0;top:27px;width:178px;font-size:5.6px;line-height:8.6px}
.icon{position:absolute;left:0;top:0;width:24px;height:24px;border:1.5px solid var(--white);border-radius:50%}
.icon::after{content:"";position:absolute;left:7px;top:7px;width:7px;height:7px;border-radius:50%;background:var(--white)}
.back-copy{font-size:5.8px;line-height:11px}
.right-copy{font-size:5.6px;line-height:8.8px}
</style>
</head>
<body>

<section class="spread spread--front" aria-label="Brochure front">
  <svg class="art" width="660" height="510" viewBox="0 0 660 510">
    <defs>
      <linearGradient id="peachFade" x1="0" y1="0" x2="1" y2="1">
        <stop offset="0" stop-color="#f29a7c"/><stop offset="1" stop-color="#ec7e61"/>
      </linearGradient>
      <linearGradient id="labPhoto" x1="0" y1="0" x2="1" y2="1">
        <stop offset="0" stop-color="#c9d8e8"/><stop offset=".5" stop-color="#7fa9d4"/><stop offset="1" stop-color="#eef2f6"/>
      </linearGradient>
      <linearGradient id="familyPhoto" x1="0" y1="0" x2="0" y2="1">
        <stop offset="0" stop-color="#6f7a4a"/><stop offset=".6" stop-color="#8a8f99"/><stop offset="1" stop-color="#4d5a3a"/>
      </linearGradient>
    </defs>
    <rect x="206" y="0" width="14" height="510" fill="var(--fold)"/>
    <path d="M0 0H220V118C180 140 120 150 60 140C35 136 15 134 0 136Z" fill="url(#peachFade)"/>
    <path d="M205 0C210 170 320 262 470 268C560 272 630 256 660 246V0Z" fill="var(--peach-light)"/>
    <path d="M215 0C220 170 330 255 470 262C560 266 630 250 660 240V0Z" fill="url(#peachFade)"/>
    <path d="M238 0C248 150 350 232 478 238C565 242 630 228 660 220V0Z" fill="url(#labPhoto)" role="img" aria-label="Photo: gloved hands holding a petri dish with a green herb"/>
    <circle cx="330" cy="166" r="92" fill="#d9d9d9"/>
    <circle cx="330" cy="166" r="88" fill="var(--white)"/>
    <circle cx="330" cy="166" r="83" fill="url(#familyPhoto)" role="img" aria-label="Photo: smiling family of four sitting outdoors"/>
    <circle cx="609" cy="291" r="40" fill="#e2e2e2"/>
    <circle cx="609" cy="291" r="36" fill="var(--white)" stroke="var(--peach)" stroke-width="2.5"/>
    <path d="M0 442C180 470 420 498 660 462V510H0Z" fill="var(--peach-light)"/>
    <path d="M0 462C200 484 440 506 660 474V510H0Z" fill="var(--peach)"/>
    <path d="M0 486C230 494 450 510 660 490V510H0Z" fill="var(--peach-deep)"/>
  </svg>

  <h2 class="block heading cover-question">What do patients' have<br>to say about their<br>experience with<br>Dr. Varga</h2>

  <div class="block" style="left:22px;top:156px;width:172px">
    <h3 class="heading">Patient Quote Area</h3>
    <div class="body-copy quote-list">
      <p class="quote">1. Dr. Elena Varga specializes in women's health and has over 25 years of experience. She is an expert in bio-identical hormone replacement therapy and has been a Dermavia bio-identical hormone pellet practitioner for over 10 years.</p>
      <p class="quote">2. Dr. Elena Varga specializes in women's health and has over 25 years of experience. She is an expert in bio-identical hormone replacement therapy and has been a Dermavia bio-identical hormone pellet practitioner for over 10 years.</p>
      <p class="quote">3. Dr. Elena Varga specializes in women's health and has over 25 years of experience. She is an expert in bio-identical hormone replacement therapy and has been a Dermavia bio-identical hormone pellet practitioner for over 10 years.</p>
      <p class="quote">4. Dr. Elena Varga specializes in women's health and has over 25 years of experience. She is an expert in bio-identical hormone replacement therapy and has been a Dermavia bio-identical hormone pellet practitioner for over 10 years.</p>
    </div>
  </div>

  <div class="block" style="left:242px;top:262px;width:178px">
    <h3 class="heading">About Us</h3>
    <p class="body-copy" style="margin-top:3px"><strong>Dr. Elena Varga</strong> specializes in women's health and has over 25 years of experience. She is an expert in bio-identical hormone replacement therapy and has been a Dermavia bio-identical hormone pellet practitioner for over 10 years. Dr. Varga has been practicing functional medicine for many years with a primary focus on hormone therapy, medical weight loss, and lifestyle change. She has recently expanded her practice to incorporate additional services including healing with a focus on adrenal, gastrointestinal and detoxification programs. Dr. Varga is a practitioner of the Hale Method for functional medicine and works closely with Dr. Marcus Hale as her mentor in the development of individual treatment protocols for our patients. Dr. Hale has over 25 years of experience in functional medicine.</p>
  </div>

  <div class="block logo-name">Bright Path</div>

  <h1 class="block cover-title">
    <span class="line-light">Bright Path</span>
    <span class="line-bold">Functional</span>
    <span class="line-boxed">Medicine</span>
  </h1>
  <p class="block tagline">Functional medicine's aim is to heal the physical body in order to engage in our life purpose of connection and emotional and spiritual growth.</p>
</section>

<section class="spread spread--back" aria-label="Brochure back">
  <svg class="art" width="660" height="510" viewBox="0 0 660 510">
    <defs>
      <linearGradient id="peachBand" x1="0" y1="0" x2="1" y2="1">
        <stop offset="0" stop-color="#f29a7c"/><stop offset="1" stop-color="#ec7e61"/>
      </linearGradient>
      <linearGradient id="anatomyPhoto" x1="0" y1="0" x2="1" y2="1">
        <stop offset="0" stop-color="#f4f6f7"/><stop offset=".6" stop-color="#dfe7e4"/><stop offset="1" stop-color="#9ccaa8"/>
      </linearGradient>
      <linearGradient id="foodPhoto" x1="0" y1="0" x2="1" y2="1">
        <stop offset="0" stop-color="#3b3a36"/><stop offset=".5" stop-color="#7d8a4a"/><stop offset="1" stop-color="#c9763f"/>
      </linearGradient>
    </defs>
    <path d="M0 0H220V120C150 150 80 140 0 170Z" fill="url(#peachBand)"/>
    <rect x="220" y="0" width="220" height="510" fill="url(#peachBand)"/>
    <path d="M440 0H660V30C600 55 520 45 440 90Z" fill="url(#peachBand)"/>
    <circle cx="113" cy="132" r="95" fill="#d6d6d6"/>
    <circle cx="113" cy="132" r="91" fill="var(--white)"/>
    <circle cx="113" cy="132" r="86" fill="url(#anatomyPhoto)" role="img" aria-label="Photo: doctor's hand touching a green anatomy display"/>
    <circle cx="549" cy="80" r="78" fill="#d6d6d6"/>
    <circle cx="549" cy="80" r="74" fill="var(--white)"/>
    <circle cx="549" cy="80" r="69" fill="url(#foodPhoto)" role="img" aria-label="Photo: bowl of fresh vegetables and wholesome food"/>
    <path d="M0 480C220 498 440 500 660 462V510H0Z" fill="var(--peach-light)"/>
    <path d="M0 490C230 504 450 506 660 476V510H0Z" fill="var(--peach)"/>
    <path d="M0 500C230 508 450 512 660 492V510H0Z" fill="var(--peach-deep)"/>
  </svg>

  <div class="block" style="left:22px;top:242px;width:178px">
    <h3 class="heading">Why should you consider a<br>functional medicine visit?</h3>
    <p class="body-copy back-copy" style="margin-top:4px">You are tired of feeling tired. You can't even focus on the future because you are so overwhelmed. The pain of being unable to think clearly and being too tired to exercise are your daily reality. Your life goals seem like too much to think about, you just have to get through today.</p>
    <h3 class="heading" style="margin-top:14px">Who else you consider a<br>functional medicine visit?</h3>
    <p class="body-copy back-copy" style="margin-top:4px">You want to achieve OPTIMAL health with a personalized medicine approach. You are eating well, exercising and engaging in stress reducing activities such as meditation. You want to know how to minimize the effects of aging and are ready to take a proactive approach in getting to the highest level of health you can achieve.</p>
  </div>

  <h2 class="block heading symptoms-title">What symptoms do we treat?</h2>

  <div class="symptom" style="top:44px">
    <span class="icon"></span><h3 class="heading">Weight Gain</h3>
    <p class="body-copy">Adrenal dysfunction results in cortisol imbalance. The major function of cortisol is to help balance blood sugar. When cortisol is out of balance, your body will store body fat rather than burning fat for fuel resulting in weight gain. Menopausal hormone imbalance will also result in abdominal weight gain.</p>
  </div>
  <div class="symptom" style="top:130px">
    <span class="icon"></span><h3 class="heading">Fatigue</h3>
    <p class="body-copy">Adrenal exhaustion results from long term stress that depletes cortisol. Testing and correcting cortisol will improve energy levels. Long term stress can result in mitochondrial dysfunction and organic acid tests can tell us how to support your mitochondria.</p>
  </div>
  <div class="symptom" style="top:215px">
    <span class="icon"></span><h3 class="heading">Depression</h3>
    <p class="body-copy">We focus both on cortisol and the brain neurotransmitters dopamine, epinephrine and norepinephrine to evaluate causes of depression. Hormone imbalance can also result in both anxiety and depression.</p>
  </div>
  <div class="symptom" style="top:292px">
    <span class="icon"></span><h3 class="heading">Female Hormone Imbalance</h3>
    <p class="body-copy">Optimizing hormonal balance is our specialty. We focus on optimizing hormone levels with bio-identical hormones, but also know that adrenal treatment protocols can improve symptoms of hot flashes, night sweats, and foggy thinking.</p>
  </div>
  <div class="symptom" style="top:368px">
    <span class="icon"></span><h3 class="heading">GI Problems</h3>
    <p class="body-copy">The immune cells that line our digestive tract are regulated by cortisol. Cortisol imbalance results in inflammation and "leaky gut" causing digestive symptoms like bloating, heartburn, constipation, or diarrhea. Utilizing a comprehensive program that includes avoiding inflammatory foods and GutView stool testing allow us to find underlying infections or sources of inflammation and allow us to develop a focused treatment plan.</p>
  </div>

  <div class="block" style="left:462px;top:163px;width:178px">
    <h3 class="heading">Why should you consider<br>a what can I expect from<br>my first visit?</h3>
    <p class="body-copy right-copy" style="margin-top:4px">During your initial consultation, we want to get to know each other and find out your expectations for health. We will explore your health history and symptoms as well as lifestyle factors including diet and sleep. We will discuss your goals and reasons for getting healthy. We know that we must incorporate lifestyle changes including stress reduction, diet and exercise optimization in any program for healing. We will discuss testing recommendations including blood work, hormone evaluation, cortisol, GI, and organic acid tests as well as nutritional and personal coaching options.</p>
    <h3 class="heading" style="margin-top:12px">What are your treatment<br>protocols based on?</h3>
    <p class="body-copy right-copy" style="margin-top:4px">Treatment protocols are based on making you feel better with a focused wellness program that treats underlying cause. We want to optimize body systems by reducing inflammation, treating insulin resistance, improving catabolic physiology, and reducing oxidative stress. Treatment protocols are a combination of supplement support and hormone balance in addition to lifestyle optimization. Supplement programs tend to be focused and last approximately 6 months. Hormone programs continue for as long as you have symptoms. We will work together to determine what type of treatment program works best for you.</p>
  </div>
</section>

</body>
</html>
```